Business Card for Language School (2 locations)

We need a sleek business card for a language school that is looking to update our image to be more professional. We work with students ages Pre-Kindergarten through adults. Our idea is to have an all-black business card with white or silver lettering. On the front will be the name of our school (Bright Meadow English Academy), and on the back there will be information for our location, phone number, email, and website (and possibly social media information). We have two school branches, so the address, phone number, and email address will be different for each branch, but all of the other information will stay the same. We'd like each branch to have a different color card edge that is neon. We are also open to suggestions and new ideas!

Some answers to questions we have received:
1. The reason we haven't added a logo is because we are looking to get a new one. We hadn't originally planned to do that at this time, but we are going to look into updating our project to include that as another aspect of it. We had previously planned to just include the school name on the front without a logo at this time.
2. We currently have two branches of our school, and we want our business card design to be uniform for each location. While it might make sense to put the information on one card right now, we plan to have more locations in the future, so we want to plan ahead with a unified design right now.
3. Our school addresses and phone numbers can be found on our website: www.brightmeadowlingo.example (at the bottom of the page)!
Updates

Part of this contest is also a new logo design. Our previous design was a train, which we would be open to keeping if it had an updated, sleeker design.

Contact Information for Business Card

Card #1:
Bright Meadow English Academy (Qinglu Branch)
Fuxing W. Rd. Sec. 3, Lane 412, No. 58, 1F
Beitou District, Taipei City 11260
02-2941-3086
qinglu@brightmeadowlingo.example

Card #2:
Bright Meadow English Academy (Heping Branch)
Linsen Road, No. 318, 1F
Songshan District, Taipei City 10587
02-2764-1520
heping@brightmeadowlingo.example

Both cards:
Website: www.brightmeadowlingo.example
Facebook: www.facebook.com/brightmeadowlingo
Instagram: @brightmeadowlingo

```html
<!DOCTYPE html>
<html lang="en">
<head>
<meta charset="utf-8">
<title>Bright Meadow English Academy — Business Card</title>
<link href="https://fonts.googleapis.com/css2?family=Jost:wght@300;400;600;700&display=swap" rel="stylesheet">
<style>
  :root {
    --bg: #1a1a1a;
    --card: #262626;
    --card-light: #333333;
    --edge: #29abe2;
    --brand: #1e90d8;
    --accent: #29abe2;
    --ink: #f2f2f2;
  }
  * { box-sizing: border-box; margin: 0; padding: 0; }
  html, body {
    width: 1200px; height: 900px; overflow: hidden;
    background: var(--bg);
    font-family: "Jost", sans-serif;
    color: var(--ink);
  }
  .canvas {
    width: 1200px; height: 900px;
    display: flex; flex-direction: column;
    align-items: center; justify-content: center; gap: 40px;
  }
  .card {
    position: relative;
    width: 700px; height: 400px;
    background: radial-gradient(circle at 75% 35%, var(--card-light), var(--card) 65%);
    border-bottom: 7px solid var(--edge);
    box-shadow: 0 18px 40px rgba(0,0,0,0.6);
    overflow: hidden;
  }

  .wordmark { display: flex; align-items: center; gap: 22px; }
  .wordmark-square { background: var(--brand); flex: none; }
  .wordmark-name {
    color: var(--brand); font-weight: 600; line-height: 0.98;
  }

  .card-front { display: flex; align-items: center; justify-content: center; }
  .card-front .wordmark-square { width: 110px; height: 110px; }
  .card-front .wordmark-name { font-size: 46px; }

  .card-back .branch { position: absolute; left: 50px; top: 44px; }
  .branch-school { color: var(--accent); font-size: 23px; font-weight: 600; }
  .branch-name { color: var(--ink); font-size: 20px; font-weight: 600; margin-top: 2px; }

  .address {
    position: absolute; left: 50px; top: 140px;
    font-size: 20px; font-weight: 300; line-height: 1.35; font-style: normal;
  }
  .contacts {
    position: absolute; left: 50px; top: 262px;
    list-style: none; font-size: 18px; font-weight: 300; line-height: 1.45;
  }
  .contacts li { display: flex; align-items: center; gap: 12px; }
  .contacts svg { width: 14px; height: 14px; flex: none; }

  .card-back .wordmark { position: absolute; right: 46px; top: 120px; gap: 14px; }
  .card-back .wordmark-square { width: 52px; height: 52px; }
  .card-back .wordmark-name { font-size: 24px; }

  .social {
    position: absolute; right: 46px; bottom: 36px;
    font-size: 19px; font-weight: 300; line-height: 1.4;
  }
  .social dt { color: var(--accent); font-weight: 600; display: inline; }
  .social dd { display: inline; }
  .social div { text-align: left; }
</style>
</head>
<body>
<main class="canvas">

  <section class="card card-front" aria-label="Card front">
    <div class="wordmark">
      <span class="wordmark-square" aria-hidden="true"></span>
      <p class="wordmark-name">Bright Meadow<br>English<br>Academy</p>
    </div>
  </section>

  <section class="card card-back" aria-label="Card back">
    <header class="branch">
      <p class="branch-school">Bright Meadow English Academy</p>
      <p class="branch-name">(Qinglu Branch)</p>
    </header>

    <address class="address">
      Fuxing W. Rd. Sec. 3,<br>
      Lane 412, No. 58, 1F<br>
      Beitou District, Taipei City 11260
    </address>

    <ul class="contacts">
      <li>
        <svg viewBox="0 0 16 16" aria-hidden="true"><path d="M4 1.5l2.2 3-1.3 1.6a8 8 0 0 0 5 5l1.6-1.3 3 2.2-1.2 2.2C8 14.5 1.5 8 1.8 2.7z" fill="var(--accent)"/></svg>
        02-2941-3086
      </li>
      <li>
        <svg viewBox="0 0 16 16" aria-hidden="true"><rect x="1.5" y="3.5" width="13" height="9" fill="none" stroke="var(--accent)" stroke-width="1.4"/><path d="M1.5 3.5l6.5 5 6.5-5" fill="none" stroke="var(--accent)" stroke-width="1.4"/></svg>
        qinglu@brightmeadowlingo.example
      </li>
      <li>
        <svg viewBox="0 0 16 16" aria-hidden="true"><g fill="none" stroke="var(--accent)" stroke-width="1.3"><circle cx="8" cy="8" r="6.5"/><ellipse cx="8" cy="8" rx="2.8" ry="6.5"/><path d="M1.5 8h13M2.5 4.8h11M2.5 11.2h11"/></g></svg>
        www.brightmeadowlingo.example
      </li>
    </ul>

    <div class="wordmark">
      <span class="wordmark-square" aria-hidden="true"></span>
      <p class="wordmark-name">Bright Meadow<br>English<br>Academy</p>
    </div>

    <dl class="social">
      <div><dt>Fb:</dt> <dd>/brightmeadowlingo</dd></div>
      <div><dt>Ins:</dt> <dd>@brightmeadowlingo</dd></div>
    </dl>
  </section>

</main>
</body>
</html>
```